Velqa Structural Approval Standards Private Assessors

Professional Construction Consultancy Company Business Card - must keep logo colours see images below - examples have been added from my last competition - please see them as examples only!

Target Market(s)

Home Builders

Industry/Entity Type

Construction

Contact Information for Business Card

See "must haves"

Font styles to use
Sans Serif

Colors
ffffff
add136
000000

Requirements
Must have
• Daniel Moravi
• Director
• Phone: 0431 587 219
• Address: 7 Tarrunga Rd,
• Hallworth Vale, SA, 5091
• Email: velqaassessors@mailbox-example.com
• Website: www.velqaassessors-example.com.au
• Facebook: Velqa Structural Approval Standards
Nice to have
• Side 1: full logo
• Side 2: company details
Should not have
• hard to read
• must be clear and professional

```html
<!DOCTYPE html>
<html lang="en">
<head>
<meta charset="utf-8">
<title>Velqa Structural Approval Standards – Business Card</title>
<link rel="stylesheet" href="https://fonts.googleapis.com/css2?family=Lato:wght@400;700;900&family=Roboto+Condensed:wght@700&display=swap">
<style>
  :root {
    --white: #ffffff;
    --green: #add136;
    --green-deep: #8fb62a;
    --black: #000000;
    --ink: #1a1a1a;
    --stage: #e9e9e6;
  }
  * { box-sizing: border-box; margin: 0; padding: 0; }
  html, body { width: 1200px; height: 780px; overflow: hidden; }
  body {
    background: var(--stage);
    font-family: "Lato", Arial, sans-serif;
    color: var(--ink);
    position: relative;
  }
  .card {
    position: absolute;
    top: 226px;
    width: 540px;
    height: 328px;
    background: var(--white);
    border-radius: 14px;
    overflow: hidden;
    box-shadow: 0 10px 26px rgba(0,0,0,.18);
  }
  .card--details { left: 40px; }
  .card--logo { left: 620px; }
  .card__art { position: absolute; inset: 0; width: 100%; height: 100%; }

  /* company name block */
  .wordmark {
    position: absolute;
    display: flex;
    align-items: center;
    gap: 12px;
    font-family: "Lato", Arial, sans-serif;
    font-weight: 900;
    color: var(--black);
    text-transform: uppercase;
    white-space: nowrap;
  }
  .wordmark__square {
    width: 44px; height: 44px;
    background: var(--green);
    flex: none;
  }
  .wordmark__text { display: flex; flex-direction: column; line-height: 1; }
  .wordmark__initials { font-size: 46px; letter-spacing: 1px; }
  .wordmark__line { font-size: 13px; letter-spacing: .5px; margin-top: 4px; }
  .wordmark__tag { font-size: 11px; letter-spacing: 4.5px; margin-top: 6px; }

  .card--details .wordmark { left: 30px; top: 134px; }
  .card--logo .wordmark { left: 50%; top: 50%; transform: translate(-50%, -50%); }
  .card--logo .wordmark__initials { font-size: 52px; }
  .card--logo .wordmark__line { font-size: 14px; }
  .card--logo .wordmark__square { width: 50px; height: 50px; }

  /* contact details */
  .contact {
    position: absolute;
    right: 26px;
    top: 22px;
    text-align: right;
    font-size: 12.5px;
    line-height: 1.45;
    white-space: nowrap;
  }
  .contact__name {
    font-family: "Roboto Condensed", Arial, sans-serif;
    font-weight: 700;
    font-size: 19px;
    letter-spacing: .5px;
    text-transform: uppercase;
    color: var(--black);
    line-height: 1.1;
  }
  .contact__role { color: var(--green-deep); font-size: 13px; margin-bottom: 10px; }
  .contact__row { display: flex; justify-content: flex-end; align-items: center; gap: 7px; }
  .contact__icon {
    width: 13px; height: 13px;
    background: var(--green);
    border-radius: 2px;
    flex: none;
  }
  .contact__icon svg { display: block; width: 13px; height: 13px; }

  .website {
    position: absolute;
    right: 26px;
    bottom: 24px;
    font-size: 12.5px;
    color: var(--black);
    letter-spacing: .3px;
    white-space: nowrap;
  }
</style>
</head>
<body>

  <!-- Side 2: company details -->
  <section class="card card--details" aria-label="Business card, details side">
    <svg class="card__art" viewBox="0 0 540 328" aria-hidden="true">
      <path d="M0,268 Q300,258 540,206 L540,328 L0,328 Z" fill="var(--green)"/>
      <path d="M0,246 Q290,240 520,170 Q320,236 0,262 Z" fill="var(--black)"/>
    </svg>

    <div class="wordmark">
      <span class="wordmark__square"></span>
      <span class="wordmark__text">
        <span class="wordmark__initials">Velqa</span>
        <span class="wordmark__line">Structural Approval Standards</span>
        <span class="wordmark__tag">Private Assessors</span>
      </span>
    </div>

    <div class="contact">
      <p class="contact__name">Daniel Moravi</p>
      <p class="contact__role">Director</p>
      <p>7 Tarrunga Rd,</p>
      <p>Hallworth Vale, SA, 5091</p>
      <p class="contact__row">0431 587 219
        <span class="contact__icon"><svg viewBox="0 0 13 13" aria-label="Phone"><path d="M3.6,2.5 L5.2,4.4 L4.4,5.4 Q5.4,7.4 7.6,8.6 L8.6,7.8 L10.5,9.4 L9.6,10.6 Q5.6,10.2 2.4,3.4 Z" fill="var(--white)"/></svg></span>
      </p>
      <p class="contact__row">velqaassessors@mailbox-example.com
        <span class="contact__icon"><svg viewBox="0 0 13 13" aria-label="Email"><rect x="2.5" y="3.5" width="8" height="6" fill="none" stroke="var(--white)" stroke-width="1"/><path d="M2.5,3.5 L6.5,7 L10.5,3.5" fill="none" stroke="var(--white)" stroke-width="1"/></svg></span>
      </p>
      <p class="contact__row">Velqa Structural Approval Standards
        <span class="contact__icon" aria-label="Social page"></span>
      </p>
    </div>

    <p class="website">www.velqaassessors-example.com.au</p>
  </section>

  <!-- Side 1: full name -->
  <section class="card card--logo" aria-label="Business card, name side">
    <svg class="card__art" viewBox="0 0 540 328" aria-hidden="true">
      <path d="M0,0 L540,0 L540,92 Q260,66 0,22 Z" fill="var(--green)"/>
      <path d="M40,40 Q300,84 540,104 L540,118 Q280,98 40,40 Z" fill="var(--black)"/>
      <path d="M0,328 L540,328 L540,306 Q280,262 0,236 Z" fill="var(--green)"/>
      <path d="M0,224 Q260,246 500,288 Q240,232 0,210 Z" fill="var(--black)"/>
    </svg>

    <div class="wordmark">
      <span class="wordmark__square"></span>
      <span class="wordmark__text">
        <span class="wordmark__initials">Velqa</span>
        <span class="wordmark__line">Structural Approval Standards</span>
        <span class="wordmark__tag">Private Assessors</span>
      </span>
    </div>
  </section>

</body>
</html>
```